Bus Card - T.K. Gate Co
T.K. Gate Co
Project: Bus Card - T.K. Gate Co
Creative Brief
Professional
Owner
4172 Pelton Lane Berkeley Springs, WV 25411
tkmorrowventures@mailpost.example
Would prefer a design for wooden business cards.

```html
<!DOCTYPE html>
<html lang="en">
<head>
<meta charset="utf-8">
<title>T.K. Gate Co — Business Card</title>
<link href="https://fonts.googleapis.com/css2?family=Poppins:wght@400;600&display=swap" rel="stylesheet">
<style>
  :root {
    --backdrop: #2b2b2d;
    --card: #f7f7f5;
    --ink: #1f3d2b;
    --text: #2e2e2e;
    --muted: #555555;
  }
  * { margin: 0; padding: 0; box-sizing: border-box; }
  html, body { width: 1200px; height: 1057px; overflow: hidden; }
  body {
    background: var(--backdrop);
    font-family: "Poppins", Arial, sans-serif;
    color: var(--text);
    display: flex;
    flex-direction: column;
    align-items: center;
    justify-content: center;
    gap: 40px;
  }
  .card {
    width: 860px;
    height: 470px;
    background: var(--card);
    border-radius: 26px;
    position: relative;
    overflow: hidden;
    box-shadow: 0 10px 24px rgba(0,0,0,.35);
  }
  /* Front */
  .front-info { position: absolute; left: 60px; top: 48px; }
  .accent-bar {
    position: absolute; left: 0; top: 52px;
    width: 14px; height: 62px; background: var(--ink);
  }
  .company-name { font-size: 34px; font-weight: 600; color: var(--ink); line-height: 1.2; }
  .role { font-size: 15px; color: var(--muted); margin-top: 4px; }
  .address { font-size: 17px; line-height: 1.6; margin-top: 70px; }
  .contacts { list-style: none; margin-top: 58px; font-size: 17px; line-height: 1.75; }
  .contacts li { display: flex; align-items: center; gap: 12px; }
  .contacts svg { width: 16px; height: 16px; flex: none; }
  .wordmark {
    font-weight: 600; color: var(--ink);
    letter-spacing: 1px; text-align: center; white-space: nowrap;
  }
  .front .wordmark {
    position: absolute; right: 60px; top: 200px; width: 340px; font-size: 40px;
  }
  /* Back */
  .back { display: flex; align-items: center; justify-content: center; }
  .back .wordmark { font-size: 62px; }
</style>
</head>
<body>
  <section class="card front">
    <div class="accent-bar"></div>
    <div class="front-info">
      <h1 class="company-name">T.K. Gate Co</h1>
      <p class="role">Owner</p>
      <p class="address">4172 Pelton Lane<br>Alder Springs, WV 25499</p>
      <ul class="contacts">
        <li>
          <svg viewBox="0 0 16 16" aria-hidden="true"><rect x="4" y="1" width="8" height="14" rx="1.5" fill="none" stroke="#2e2e2e" stroke-width="1.5"/><circle cx="8" cy="12.3" r=".9" fill="#2e2e2e"/></svg>
          877-555-0142
        </li>
        <li>
          <svg viewBox="0 0 16 16" aria-hidden="true"><path d="M3 2h3l1.5 3.5-2 1.3a8 8 0 0 0 3.7 3.7l1.3-2L14 10v3a1.5 1.5 0 0 1-1.6 1.5A12 12 0 0 1 1.5 3.6 1.5 1.5 0 0 1 3 2z" fill="#2e2e2e"/></svg>
          304-555-0187
        </li>
        <li>
          <svg viewBox="0 0 16 16" aria-hidden="true"><rect x="1" y="3" width="14" height="10" rx="1" fill="none" stroke="#2e2e2e" stroke-width="1.4"/><path d="M1.5 4l6.5 5 6.5-5" fill="none" stroke="#2e2e2e" stroke-width="1.4"/></svg>
          tkmorrowventures@mailpost.example
        </li>
      </ul>
    </div>
    <div class="wordmark">T.K. Gate Co</div>
  </section>

  <section class="card back">
    <div class="wordmark">T.K. Gate Co</div>
  </section>
</body>
</html>
```